Chorus of the Pacific Presents

Show name:
Bloom Melody Revue
Location:
Del Paso High School
4218 Larkmoor Ln, Citrus Heights, CA 95610
Times: 2 p.m. & 7 p.m.
Special Guests:
Hold Chord
Harbor Quartet
Brightwater Five
Ticket Prices:
VIP $35.00
General $25.00
Student $15.00

```html
<!DOCTYPE html>
<html lang="en">
<head>
<meta charset="utf-8">
<title>Bloom Melody Revue — Chorus of the Pacific</title>
<link href="https://fonts.googleapis.com/css2?family=Archivo+Black&family=Dancing+Script:wght@700&family=Michroma&display=swap" rel="stylesheet">
<style>
  :root{
    --plum:#4f0a36;
    --berry:#a31f6b;
    --magenta:#e0198a;
    --pink-light:#f0a6cc;
    --sky:#7fb3e3;
    --mist:#e9eef6;
    --white:#ffffff;
    --teal-petal:#3fc3df;
    --lilac-petal:#d4a9dc;
    --ticket:#f7b128;
  }
  *{margin:0;padding:0;box-sizing:border-box}
  html,body{width:927px;height:1200px;overflow:hidden;background:var(--white)}
  .flyer{
    position:relative;width:927px;height:1200px;overflow:hidden;
    background:
      linear-gradient(90deg, rgba(255,255,255,0) 60%, rgba(127,179,227,.85) 100%),
      linear-gradient(180deg, var(--white) 0%, var(--mist) 40%, #dde6f2 70%, var(--white) 100%);
    color:var(--plum);
    font-family:"Michroma", sans-serif;
  }
  .abs{position:absolute}
  .presenter{top:52px;left:0;width:927px;text-align:center;font-size:19px;color:var(--plum);letter-spacing:.5px}
  .hero-art{left:0;top:93px;width:318px;height:330px;
    background:radial-gradient(ellipse at 50% 50%, #ffffff 0%, #ececec 45%, rgba(225,228,234,0) 70%)}
  .flower{border-radius:50%}
  .flower--pink{left:618px;top:98px;width:116px;height:112px;background:radial-gradient(circle,#f5d44a 0 10%,#e05bb5 12%,#c93a97 70%,rgba(201,58,151,0) 72%)}
  .flower--teal{left:261px;top:601px;width:74px;height:74px;background:radial-gradient(circle,#f5d44a 0 12%,var(--teal-petal) 14%,#2aa9cf 68%,rgba(42,169,207,0) 71%)}
  .flower--lilac{left:605px;top:601px;width:74px;height:74px;background:radial-gradient(circle,#f5d44a 0 12%,var(--lilac-petal) 14%,#b98ccb 68%,rgba(185,140,203,0) 71%)}
  .meadow{left:0;top:880px;width:927px;height:320px;
    background:linear-gradient(180deg, rgba(255,255,255,0) 0%, rgba(246,196,222,.55) 45%, rgba(233,150,200,.6) 75%, rgba(240,220,230,.7) 100%)}
  .bloom-corner{left:-60px;top:950px;width:300px;height:300px;
    background:radial-gradient(circle at 10% 90%, #f3d23d 0 14%, var(--teal-petal) 16%, #27aed4 55%, rgba(39,174,212,0) 72%)}
  .title{left:0;top:0;width:927px;height:600px}
  .title .script{font-family:"Dancing Script", cursive;font-weight:700}
  .title .block{font-family:"Archivo Black", sans-serif}
  .location-label{top:622px;left:0;width:927px;text-align:center;font-family:"Archivo Black", sans-serif;font-size:28px;letter-spacing:1.5px;color:var(--plum)}
  .venue{left:0;width:927px;text-align:center;color:var(--plum)}
  .venue--name{top:663px;font-size:16px}
  .venue--address{top:688px;font-size:15px;letter-spacing:.2px}
  .times{top:716px;left:0;width:927px;text-align:center;font-family:"Archivo Black", sans-serif;font-size:27px;color:var(--berry);letter-spacing:2.5px}
  .times .amp{font-size:14px}
  .section-head{top:764px;font-family:"Archivo Black", sans-serif;font-size:26px;color:var(--plum);letter-spacing:1px}
  .section-head--guests{left:130px}
  .section-head--tickets{left:525px}
  .guest-icon{left:116px;top:805px;width:88px;height:80px}
  .list{font-size:15px;line-height:25px;color:var(--plum);list-style:none}
  .guest-list{left:211px;top:807px}
  .ticket-art{left:494px;top:804px;width:100px;height:78px;border-radius:6px;
    background:linear-gradient(160deg,#fcc64a 0%,var(--ticket) 60%,#e89a1a 100%);transform:rotate(-8deg)}
  .price-list{left:609px;top:807px}
  .price-list li{display:grid;grid-template-columns:116px auto;column-gap:6px}
</style>
</head>
<body>
<main class="flyer">
  <div class="abs hero-art" role="img" aria-label="Sketched hand raising a microphone against white sunburst rays"></div>
  <div class="abs meadow" role="img" aria-label="Soft-focus field of pink cosmos flowers against a pale sky"></div>
  <div class="abs bloom-corner" role="img" aria-label="Large turquoise daisy with a golden centre in the corner"></div>
  <div class="abs flower flower--pink" role="img" aria-label="Pink daisy"></div>

  <p class="abs presenter">CHORUS OF THE PACIFIC PRESENTS</p>

  <svg class="abs title" viewBox="0 0 927 600" aria-label="Bloom Melody Revue">
    <defs>
      <linearGradient id="scriptFill" x1="0" y1="0" x2="1" y2="1">
        <stop offset="0" stop-color="var(--pink-light)"/>
        <stop offset=".5" stop-color="var(--magenta)"/>
        <stop offset="1" stop-color="var(--berry)"/>
      </linearGradient>
    </defs>
    <text class="script" x="335" y="345" font-size="175" fill="url(#scriptFill)" textLength="435" lengthAdjust="spacingAndGlyphs">Bloom</text>
    <path d="M470 365 Q560 345 640 352" stroke="var(--magenta)" stroke-width="7" fill="none" stroke-linecap="round"/>
    <text class="block" x="163" y="511" font-size="172" fill="var(--berry)" textLength="619" lengthAdjust="spacingAndGlyphs">MELODY</text>
    <text class="block" x="144" y="582" font-size="78" fill="var(--plum)" textLength="627" lengthAdjust="spacingAndGlyphs">REVUE</text>
  </svg>

  <div class="abs flower flower--teal" role="img" aria-label="Turquoise daisy"></div>
  <div class="abs flower flower--lilac" role="img" aria-label="Lilac daisy"></div>

  <h2 class="abs location-label">LOCATION:</h2>
  <p class="abs venue venue--name">DEL PASO HIGH SCHOOL</p>
  <p class="abs venue venue--address">4218 LARKMOOR LN, CITRUS HEIGHTS, CA 95610</p>
  <p class="abs times">TIMES: 2 P.M. <span class="amp">&amp;</span> 7 P.M.</p>

  <h2 class="abs section-head section-head--guests">SPECIAL GUESTS:</h2>
  <svg class="abs guest-icon" viewBox="0 0 88 80" aria-hidden="true">
    <path d="M10 30 A36 36 0 0 1 78 30" fill="none" stroke="var(--plum)" stroke-width="4"/>
    <path d="M78 50 A36 36 0 0 1 10 50" fill="none" stroke="var(--plum)" stroke-width="4"/>
    <path d="M2 28 L10 40 L18 28 Z" fill="var(--plum)"/>
    <path d="M70 52 L78 40 L86 52 Z" fill="var(--plum)"/>
    <circle cx="30" cy="31" r="6" fill="var(--plum)"/>
    <circle cx="58" cy="31" r="6" fill="var(--plum)"/>
    <path d="M20 58 Q20 40 30 40 Q40 40 40 58 Z" fill="var(--plum)"/>
    <path d="M48 58 Q48 40 58 40 Q68 40 68 58 Z" fill="var(--plum)"/>
    <circle cx="44" cy="27" r="8" fill="var(--plum)" stroke="var(--white)" stroke-width="2"/>
    <path d="M30 62 Q30 38 44 38 Q58 38 58 62 Z" fill="var(--plum)" stroke="var(--white)" stroke-width="2"/>
  </svg>
  <ul class="abs list guest-list">
    <li>HOLD CHORD</li>
    <li>HARBOR QUARTET</li>
    <li>BRIGHTWATER FIVE</li>
  </ul>

  <h2 class="abs section-head section-head--tickets">TICKET PRICES:</h2>
  <div class="abs ticket-art" role="img" aria-label="Pair of orange admission tickets"></div>
  <ul class="abs list price-list">
    <li><span>VIP</span><span>$35.00</span></li>
    <li><span>GENERAL</span><span>$25.00</span></li>
    <li><span>STUDENT</span><span>$15.00</span></li>
  </ul>
</main>
</body>
</html>
```